Sticker mit Text
Zielgruppe
Buchverkauf
Aufgabenstellung
Das Design soll als Sticker in Pakete geklebt werden. Hierfür verwenden wir Die Cut Sticker von Klebfuchs in einer Formatgröße von etwa 10x10cm. https://www.klebfuchs.example/products/die-cut-stickers
Auf dem Sticker soll folgender Text enthalten sein:
Haben Sie es gewusst? Es gibt nur 4 giftige Vogelarten.
Der Pitohui ist einer von ihnen. Er ist giftig, weil er giftige Käfer frisst. Je mehr er davon verspeist, desto giftiger wird er.
Was manche Käufer bei Kaufwelt vielleicht auch nicht wissen, dass sich ein Verkäufer prima durch eine Sterne-Bewertung unterstützen lässt. Probieren Sie es aus. Wenden Sie hierfür vorsichtig die Feder des Pitohui!
Von der Umrandung des Stickers sollte man einen Vogel erkennen können. Ggf. lässt sich ein Vogel aber auch in den Sticker integrieren.

```html
<!DOCTYPE html>
<html lang="de">
<head>
<meta charset="utf-8">
<title>Sticker Pitohui – Varianten</title>
<link rel="stylesheet" href="https://fonts.googleapis.com/css2?family=Oswald:wght@600&family=Source+Sans+3:wght@400&family=Courier+Prime:wght@700&display=swap">
<style>
  :root {
    --bg: #d2cfca;
    --paper: #ffffff;
    --ink: #1d1d1b;
    --orange: #dc6b2f;
    --sand: #c8bb8e;
    --teal: #63aeb7;
    --shadow: #9c9995;
    --frame: #6b6b6b;
  }
  html, body {
    margin: 0;
    padding: 0;
    width: 849px;
    height: 1200px;
    overflow: hidden;
    background: var(--bg);
  }
  .sheet {
    position: relative;
    width: 849px;
    height: 1200px;
  }
  .sticker {
    position: absolute;
    width: 304px;
    height: 304px;
  }
  .sticker--square {
    background: var(--paper);
    box-shadow: 3px 3px 0 var(--shadow);
  }
  .sticker--framed::before {
    content: "";
    position: absolute;
    inset: 4px;
    border: 1px solid var(--frame);
  }
  .sticker--one { left: 98px; top: 210px; }
  .sticker--two { left: 500px; top: 230px; }
  .sticker--three { left: 100px; top: 610px; }
  .sticker--four { left: 447px; top: 610px; }

  .disc {
    position: absolute;
    left: 44px;
    top: 61px;
    width: 218px;
    height: 218px;
    border-radius: 50%;
  }
  .disc--orange { background: var(--orange); }
  .disc--sand { background: var(--sand); }
  .disc--teal { background: var(--teal); }

  .sticker--two .disc {
    left: 4px;
    top: 41px;
    box-shadow: 0 0 0 7px var(--paper), 2px 3px 3px 7px rgba(0,0,0,0.12);
  }
  .bird-outline {
    position: absolute;
    left: -17px;
    top: -7px;
    width: 140px;
    height: 146px;
    background: var(--paper);
    border-radius: 36px 60px 20px 30px;
  }

  .bird {
    position: absolute;
    left: 29px;
    top: 23px;
    width: 128px;
    height: 130px;
    background: var(--ink);
    border-radius: 30px 56px 14px 24px;
  }
  .sticker--two .bird { left: -12px; top: -1px; width: 128px; height: 134px; }

  .message {
    position: absolute;
    left: 78px;
    top: 138px;
    width: 175px;
    color: var(--paper);
    margin: 0;
  }
  .message p { margin: 0 0 7px; }
  .message--bold {
    font-family: "Oswald", sans-serif;
    font-weight: 600;
    text-transform: uppercase;
    font-size: 5.6px;
    line-height: 7.3px;
    letter-spacing: 0.1px;
  }
  .message--sans {
    font-family: "Source Sans 3", sans-serif;
    font-size: 6.6px;
    line-height: 8px;
  }
  .message--mono {
    font-family: "Courier Prime", monospace;
    font-weight: 700;
    text-transform: uppercase;
    font-size: 4.4px;
    line-height: 6.4px;
    letter-spacing: 0.2px;
  }
  .sticker--two .message { left: 36px; top: 117px; width: 170px; }
  .sticker--four .message { left: 77px; top: 135px; }

  .feather-mark {
    position: absolute;
    width: 26px;
    height: 12px;
    background: var(--paper);
    border-radius: 6px 6px 10px 10px;
    transform: skewX(-20px);
  }
  .sticker--one .feather-mark,
  .sticker--three .feather-mark,
  .sticker--four .feather-mark { left: 140px; top: 236px; }
  .sticker--two .feather-mark { left: 100px; top: 215px; }
</style>
</head>
<body>
<main class="sheet">

  <section class="sticker sticker--square sticker--framed sticker--one">
    <div class="disc disc--orange"></div>
    <div class="bird" role="img" aria-label="Silhouette eines Vogels auf einem Zweig"></div>
    <div class="message message--bold">
      <p>Haben Sie es gewusst?<br>Es gibt nur 4 giftige Vogelarten.</p>
      <p>Der Pitohui ist einer von ihnen.<br>Er ist giftig, weil er giftige Käfer frisst.<br>Je mehr er davon verspeist, desto giftiger wird er.</p>
      <p>Was manche Käufer bei Kaufwelt vielleicht auch nicht wissen,<br>dass sich ein Verkäufer prima durch eine Sterne-Bewertung<br>unterstützen lässt. Probieren Sie es aus.<br>Wenden Sie hierfür vorsichtig die Feder des Pitohui</p>
    </div>
    <div class="feather-mark" role="img" aria-label="Drei kleine Federn"></div>
  </section>

  <section class="sticker sticker--two">
    <div class="bird-outline"></div>
    <div class="disc disc--sand"></div>
    <div class="bird" role="img" aria-label="Silhouette eines Vogels auf einem Zweig"></div>
    <div class="message message--sans">
      <p>Haben Sie es gewusst?<br>Es gibt nur 4 giftig Vogelarten.</p>
      <p>Der Pitohui ist einer von ihnen.<br>Er ist giftig, weil er giftige Käfer frisst.<br>Je mehr er davon verspeist, desto giftiger wird er.</p>
      <p>Was manche Käufer bei Kaufwelt vielleicht auch nicht wissen,<br>dass sich ein Verkäufer prima durch eine Sterne-Bewertung<br>unterstützen lässt. Probieren Sie es aus.<br>Wenden Sie hierfür vorsichtig die Feder des Pitohui!</p>
    </div>
    <div class="feather-mark" role="img" aria-label="Drei kleine Federn"></div>
  </section>

  <section class="sticker sticker--square sticker--framed sticker--three">
    <div class="disc disc--sand"></div>
    <div class="bird" role="img" aria-label="Silhouette eines Vogels auf einem Zweig"></div>
    <div class="message message--mono">
      <p>Haben Sie es gewusst?<br>Es gibt nur 4 giftige Vogelarten.</p>
      <p>Der Pitohui ist einer von ihnen.<br>Er ist giftig, weil er giftige Käfer frisst.<br>Je mehr er davon verspeist, desto giftiger wird er.</p>
      <p>Was manche Käufer bei Kaufwelt vielleicht auch nicht wissen,<br>dass sich ein Verkäufer prima durch eine Sterne-Bewertung<br>unterstützen lässt. Probieren Sie es aus.<br>Wenden Sie hierfür vorsichtig die Feder des Pitohui!</p>
    </div>
    <div class="feather-mark" role="img" aria-label="Drei kleine Federn"></div>
  </section>

  <section class="sticker sticker--square sticker--four">
    <div class="disc disc--teal"></div>
    <div class="bird" role="img" aria-label="Silhouette eines Vogels auf einem Zweig"></div>
    <div class="message message--sans">
      <p>Haben Sie es gewusst?<br>Es gibt nur 4 giftig Vogelarten.</p>
      <p>Der Pitohui ist einer von ihnen.<br>Er ist giftig, weil er giftige Käfer frisst.<br>Je mehr er davon verspeist, desto giftiger wird er.</p>
      <p>Was manche Käufer bei Kaufwelt vielleicht auch nicht wissen,<br>dass sich ein Verkäufer prima durch eine Sterne-Bewertung<br>unterstützen lässt. Probieren Sie es aus.<br>Wenden Sie hierfür vorsichtig die Feder des Pitohui!</p>
    </div>
    <div class="feather-mark" role="img" aria-label="Drei kleine Federn"></div>
  </section>

</main>
</body>
</html>
```